Talbrin Business Cards

Front and back. Simon Kavelle MBA is the CEO of Talbrin Homes. Black white and grays. Logo and cool design.

Target Market(s)

Professional lenders and investors

Industry/Entity Type

Real estate developer. NO HOUSES OR ROOFS

Contact Information for Business Card

Logo, name and unique design. Front and back. Simon Kavelle MBA is the CEO of Talbrin Homes. Black white and grays. Logo and cool design.

Font styles to use
Sans Serif

Colors

Designer to choose only greyscale colors for use in the design.

Requirements
Must have
• Cool look. Not the same card I could design.
Nice to have
• Something memorable
Should not have
• Basic

```html
<!DOCTYPE html>
<html lang="en">
<head>
<meta charset="utf-8">
<title>Talbrin Homes Business Cards</title>
<link rel="stylesheet" href="https://fonts.googleapis.com/css2?family=Montserrat:wght@500;700;800&display=swap">
<style>
  :root {
    --backdrop: #8c8c8c;
    --ink: #000000;
    --paper: #ffffff;
    --swoosh-grey: #5e5e5e;
    --text: #111111;
  }
  html, body {
    margin: 0;
    padding: 0;
    width: 1160px;
    height: 1200px;
    overflow: hidden;
    background: var(--backdrop);
    font-family: "Montserrat", sans-serif;
  }
  .canvas {
    position: relative;
    width: 1160px;
    height: 1200px;
  }
  .card {
    position: absolute;
    left: 199px;
    width: 778px;
    height: 441px;
    overflow: hidden;
  }
  .card--front { top: 105px; background: var(--paper); }
  .card--back { top: 633px; background: var(--ink); }

  .front-wave {
    position: absolute;
    left: 0;
    top: 0;
    width: 778px;
    height: 441px;
  }
  .holder {
    position: absolute;
    left: 35px;
    top: 50px;
    color: var(--text);
  }
  .holder__name {
    margin: 0;
    font-size: 23px;
    font-weight: 800;
    letter-spacing: 0.2px;
    line-height: 1.1;
    white-space: nowrap;
  }
  .holder__title {
    margin: 6px 0 0;
    font-size: 18px;
    font-weight: 500;
  }
  .brand-name {
    position: absolute;
    margin: 0;
    font-family: "Montserrat", sans-serif;
    font-weight: 800;
    line-height: 1;
    white-space: nowrap;
  }
  .brand-name--front {
    right: 44px;
    top: 72px;
    font-size: 44px;
    color: var(--ink);
    letter-spacing: -0.5px;
  }
  .brand-name--back {
    left: 0;
    right: 0;
    top: 186px;
    text-align: center;
    font-size: 74px;
    color: var(--paper);
    letter-spacing: -1px;
  }
  .contacts {
    position: absolute;
    left: 35px;
    top: 214px;
    margin: 0;
    padding: 0;
    list-style: none;
  }
  .contacts__item {
    display: flex;
    align-items: center;
    height: 27px;
    margin-bottom: 10px;
    font-size: 21px;
    font-weight: 500;
    color: var(--text);
    white-space: nowrap;
  }
  .contacts__icon {
    width: 27px;
    height: 27px;
    margin-right: 13px;
    flex: none;
  }
  .address {
    position: absolute;
    right: 45px;
    top: 256px;
    margin: 0;
    font-style: normal;
    font-size: 19px;
    font-weight: 500;
    line-height: 28px;
    text-align: left;
    color: var(--text);
    white-space: nowrap;
  }
</style>
</head>
<body>
<main class="canvas">
  <section class="card card--front" aria-label="Business card front">
    <svg class="front-wave" viewBox="0 0 778 441" aria-hidden="true">
      <path fill="var(--swoosh-grey)" d="M0 311 C90 350 200 392 300 389 C350 388 390 382 413 373 C370 390 310 402 260 400 C170 397 80 370 0 346 Z"/>
      <path fill="var(--ink)" d="M0 356 C90 392 180 418 280 412 C420 402 500 322 620 328 C690 332 740 348 778 360 L778 441 L0 441 Z"/>
    </svg>

    <div class="holder">
      <h1 class="holder__name">SIMON KAVELLE MBA</h1>
      <p class="holder__title">CEO</p>
    </div>

    <p class="brand-name brand-name--front">Talbrin Homes</p>

    <ul class="contacts">
      <li class="contacts__item">
        <svg class="contacts__icon" viewBox="0 0 28 28" aria-hidden="true">
          <circle cx="14" cy="14" r="14" fill="var(--ink)"/>
          <path fill="var(--paper)" d="M7 11 C7 8 21 8 21 11 L19 12.5 L17 11 L11 11 L9 12.5 Z"/>
          <path fill="var(--paper)" d="M10 13 H18 L20 19 H8 Z"/>
          <circle cx="14" cy="16" r="1.6" fill="var(--ink)"/>
        </svg>
        <span>555-014-2736</span>
      </li>
      <li class="contacts__item">
        <svg class="contacts__icon" viewBox="0 0 28 28" aria-hidden="true">
          <circle cx="14" cy="14" r="14" fill="var(--ink)"/>
          <rect x="7" y="9" width="14" height="10" rx="1" fill="var(--paper)"/>
          <path d="M7.5 9.5 L14 15 L20.5 9.5 M7.5 18.5 L12 14 M20.5 18.5 L16 14" stroke="var(--ink)" stroke-width="1.2" fill="none"/>
        </svg>
        <span>info@marrowfield.com</span>
      </li>
      <li class="contacts__item">
        <svg class="contacts__icon" viewBox="0 0 28 28" aria-hidden="true">
          <circle cx="14" cy="14" r="14" fill="var(--ink)"/>
          <circle cx="14" cy="14" r="7.5" fill="var(--paper)"/>
          <path fill="var(--ink)" d="M10 10 C12 9 13 11 12 12.5 C11 14 13 15 12 17 C10 16 8.5 14 9 12 Z M15.5 15 C17 14.5 19 15.5 18 17.5 C17 19 15 19 15.5 17 Z"/>
        </svg>
        <span>www.marrowfield.com</span>
      </li>
    </ul>

    <address class="address">42-07 Ferrin Ave 12<br>Oakvale, NY 10950</address>
  </section>

  <section class="card card--back" aria-label="Business card back">
    <p class="brand-name brand-name--back">Talbrin Homes</p>
  </section>
</main>
</body>
</html>
```